Working Capital graphics

Our business advisory firm requires 9 images to be re-created and improved in the branding of our business.

The 9 images have been uploaded below and the colours and branding of the business can be found at the website www.thornwickadvisory.com.au

```html
<!DOCTYPE html>
<html lang="en">
<head>
<meta charset="UTF-8">
<title>Working Capital</title>
<link href="https://fonts.googleapis.com/css2?family=Quicksand:wght@500;600;700&display=swap" rel="stylesheet">
<style>
  :root {
    --orange: #f7941d;
    --blue: #00aeef;
    --ink: #2b2b2b;
    --tile-line: #f0f0f0;
    --bg: #ffffff;
  }
  html, body {
    margin: 0;
    padding: 0;
    overflow: hidden;
    background: var(--bg);
  }
  .canvas {
    position: relative;
    width: 1200px;
    height: 569px;
    overflow: hidden;
    background: var(--bg);
    font-family: "Quicksand", sans-serif;
    color: var(--ink);
  }
  .title {
    position: absolute;
    top: 62px;
    left: 0;
    width: 100%;
    margin: 0;
    text-align: center;
    font-size: 44px;
    font-weight: 700;
    letter-spacing: 0.5px;
    line-height: 1;
  }
  .title .word-working { color: var(--orange); }
  .title .word-capital { color: var(--blue); }

  .tile {
    position: absolute;
    width: 170px;
    height: 170px;
    margin: -85px 0 0 -85px;
    display: flex;
    flex-direction: column;
    align-items: center;
    justify-content: center;
    text-align: center;
  }
  .tile::before {
    content: "";
    position: absolute;
    left: 25px;
    top: 25px;
    width: 120px;
    height: 120px;
    border-radius: 20px;
    border: 1px solid var(--tile-line);
    background: var(--bg);
    transform: rotate(45deg);
    z-index: 0;
  }
  .tile--raised::before {
    border-color: transparent;
    box-shadow: 2px 6px 14px rgba(0, 0, 0, 0.08);
  }
  .tile > * { position: relative; z-index: 1; }
  .tile-icon {
    width: 37px;
    height: 48px;
    margin-bottom: 6px;
  }
  .tile-label {
    font-size: 11.5px;
    font-weight: 600;
    line-height: 1.3;
    white-space: nowrap;
  }

  .note {
    position: absolute;
    top: 476px;
    left: 0;
    width: 100%;
    margin: 0;
    text-align: center;
    font-size: 11.4px;
    font-weight: 600;
  }
</style>
</head>
<body>
<div class="canvas">
  <svg width="0" height="0" style="position:absolute" aria-hidden="true">
    <defs>
      <symbol id="shield-home" viewBox="0 0 37 48">
        <path d="M18.5 2 L34 8 V25 C34 35 27 42 18.5 46 C10 42 3 35 3 25 V8 Z" fill="none" stroke="var(--orange)" stroke-width="2.4" stroke-linejoin="round"/>
        <path d="M18.5 7 L29.5 11.5 V25 C29.5 32.5 24.5 38 18.5 41 C12.5 38 7.5 32.5 7.5 25 V11.5 Z" fill="none" stroke="var(--orange)" stroke-width="2" stroke-linejoin="round"/>
        <path d="M11.5 24 L18.5 17 L25.5 24 M13.5 22 V30 H23.5 V22" fill="none" stroke="var(--blue)" stroke-width="2.2" stroke-linecap="round" stroke-linejoin="round"/>
        <path d="M17 30 V26 H20 V30" fill="none" stroke="var(--blue)" stroke-width="1.8"/>
      </symbol>
    </defs>
  </svg>

  <h1 class="title"><span class="word-working">Working</span> <span class="word-capital">Capital</span></h1>

  <div class="tile tile--raised" style="left:223px;top:242px">
    <svg class="tile-icon"><use href="#shield-home"/></svg>
    <div class="tile-label">Supply<br>Chain Issues</div>
  </div>
  <div class="tile" style="left:410px;top:242px">
    <svg class="tile-icon"><use href="#shield-home"/></svg>
    <div class="tile-label">Forecasting<br>And Planning</div>
  </div>
  <div class="tile" style="left:597px;top:242px">
    <svg class="tile-icon"><use href="#shield-home"/></svg>
    <div class="tile-label">SKU Complexity</div>
  </div>
  <div class="tile" style="left:784px;top:242px">
    <svg class="tile-icon"><use href="#shield-home"/></svg>
    <div class="tile-label">KPIs Measures</div>
  </div>
  <div class="tile" style="left:972px;top:242px">
    <svg class="tile-icon"><use href="#shield-home"/></svg>
    <div class="tile-label">Terms<br>And Conditions</div>
  </div>

  <div class="tile" style="left:316px;top:353px">
    <svg class="tile-icon"><use href="#shield-home"/></svg>
    <div class="tile-label">Process Issues</div>
  </div>
  <div class="tile" style="left:503px;top:353px">
    <svg class="tile-icon"><use href="#shield-home"/></svg>
    <div class="tile-label">Customer<br>Management</div>
  </div>
  <div class="tile" style="left:690px;top:353px">
    <svg class="tile-icon"><use href="#shield-home"/></svg>
    <div class="tile-label">Supplier<br>Management</div>
  </div>
  <div class="tile" style="left:877px;top:353px">
    <svg class="tile-icon"><use href="#shield-home"/></svg>
    <div class="tile-label">IT Systems<br>&amp; Information</div>
  </div>

  <p class="note">Note: Icons used are dummy and are for presentation purpose only....Once you like the design...icons will be replaced.</p>
</div>
</body>
</html>
```